Post Card Design - Photo on front, details on back. Logo on both sides.

Back: See the photo of my old card. The back worked well, as it gave me lots of space to write on. The address details are still correct, but the logo has changed to Josephine Sans. Logo can be on one line or on two (if two, align it on the left).
Don't include the 'BEAUTIFUL WEDDING DRESSES...' bit.
I'd like to print this on thicker, slightly coarse paper, so don't go too small on detail.
Here are the Quorl paper details: Paper Stock: Natural Uncoated
Paper Thickness: Premium
Finish: None
Front of Card: I'd like to see options for both pictures:
I think the painted image would look best with a frame in a pale shade and the logo in the frame fairly subtle.
The actual dress photo I'd like to see cropped a bit like in my mock up. You'll need to have a look at how the logo would be best placed on this. You can place it anywhere, or add a banner.
See my website for my brand's look: lorabetwick.co.nz
Target Market(s)
Brides
Industry/Entity Type
Wedding Dresses
Contact Information for Business Card
Front: Photo and logo. Back: with details and lots of empty space. See attached photos for loose brief.
Other font styles liked:
- Josephine Sans
Requirements
Must have
- I hand-write the gown designs and price on the back of the card, so there needs to be plenty of empty space.
Nice to have
- As per brief.
Should not have
- It must look clean, romantic, modern. Timeless.

```html
<!DOCTYPE html>
<html lang="en">
<head>
<meta charset="utf-8">
<title>Lora Betwick — Business Cards</title>
<link href="https://fonts.googleapis.com/css2?family=Josefin+Sans:wght@300&family=Mulish:wght@400&display=swap" rel="stylesheet">
<style>
  :root {
    --bg-upper: #e9eaed;
    --bg-lower: #cdb8a3;
    --card-white: #ffffff;
    --card-cream: #f0dfb8;
    --edge-gold: #a8842f;
    --ink: #1c1c1c;
    --ink-light: #ffffff;
    --photo-light: #f1e4d3;
    --photo-mid: #d9bd9c;
    --photo-deep: #b89270;
    --paint-rose: #ec9aa2;
    --paint-peach: #f2c3a0;
    --paint-ivory: #f6ecd9;
  }
  * { margin: 0; padding: 0; box-sizing: border-box; }
  html, body { width: 1200px; height: 2268px; overflow: hidden; }
  body { font-family: "Josefin Sans", sans-serif; color: var(--ink); }

  .presentation { position: relative; width: 1200px; height: 1134px; }
  .presentation--photo { background: var(--bg-upper); }
  .presentation--painted { background: var(--bg-lower); }

  .card {
    position: absolute;
    left: 210px;
    width: 780px;
    height: 446px;
    border-bottom: 4px solid var(--edge-gold);
    box-shadow: 0 14px 30px rgba(0,0,0,0.18);
    overflow: hidden;
  }
  .card--front { top: 80px; }
  .card--back { top: 610px; background: var(--card-white); }

  .front-photo {
    position: absolute; inset: 0;
    background:
      linear-gradient(115deg, rgba(255,255,255,0.35) 0%, rgba(255,255,255,0) 35%),
      linear-gradient(160deg, var(--photo-light) 0%, var(--photo-mid) 45%, var(--photo-deep) 70%, var(--photo-light) 100%);
  }
  .card--front-painted { background: var(--card-cream); }
  .front-painting {
    position: absolute;
    left: 300px; top: 70px;
    width: 440px; height: 330px;
    border-radius: 50%;
    background: radial-gradient(ellipse at 45% 45%, var(--paint-rose) 0%, var(--paint-peach) 40%, var(--paint-ivory) 70%, rgba(240,223,184,0) 100%);
  }

  .logo-vertical {
    position: absolute;
    left: 46px; top: 34px;
    writing-mode: vertical-rl;
    font-family: "Josefin Sans", sans-serif;
    font-weight: 300;
    line-height: 0.95;
    text-transform: uppercase;
    letter-spacing: 0.04em;
  }
  .logo-vertical .logo-first { font-size: 92px; }
  .logo-vertical .logo-last { font-size: 64px; }
  .logo-vertical--light { color: var(--ink-light); }
  .logo-vertical--dark { color: var(--ink); }

  .logo-line {
    position: absolute;
    left: 48px; top: 46px;
    font-family: "Josefin Sans", sans-serif;
    font-weight: 300;
    font-size: 36px;
    letter-spacing: 0.06em;
    text-transform: uppercase;
  }

  .contact-list {
    position: absolute;
    right: 64px; bottom: 44px;
    list-style: none;
    font-family: "Mulish", sans-serif;
    font-size: 27px;
    line-height: 1.3;
  }
  .contact-list li { display: flex; align-items: center; gap: 10px; }
  .contact-list svg { width: 18px; height: 18px; flex: none; }
</style>
</head>
<body>

<section class="presentation presentation--photo">
  <div class="card card--front">
    <div class="front-photo" role="img" aria-label="Cropped photograph of a bride in a flowing ivory wedding gown in a sunlit room"></div>
    <div class="logo-vertical logo-vertical--light">
      <span class="logo-first">Lora</span>
      <span class="logo-last">Betwick</span>
    </div>
  </div>
  <div class="card card--back">
    <div class="logo-line">Lora Betwick</div>
    <ul class="contact-list">
      <li><svg viewBox="0 0 16 16" aria-hidden="true"><path d="M4 1.5c.7 0 1.4 2.6 1 3.2L3.8 5.8c.8 2 2.3 3.6 4.3 4.5l1.1-1.2c.6-.5 3.3.3 3.3 1v1.7c0 .8-.8 1.5-1.7 1.4C5.8 12.6 2.2 9 1.6 4.1 1.5 3.2 2.2 2.4 3 2.4z" fill="#1c1c1c"/></svg>+64 9 555 0147</li>
      <li><svg viewBox="0 0 16 16" aria-hidden="true"><g fill="none" stroke="#1c1c1c" stroke-width="1.3"><circle cx="8" cy="8" r="6.5"/><ellipse cx="8" cy="8" rx="3" ry="6.5"/><path d="M1.5 8h13M2.5 4.5h11M2.5 11.5h11"/></g></svg>lorabetwick.co.nz</li>
      <li><svg viewBox="0 0 16 16" aria-hidden="true"><g fill="none" stroke="#1c1c1c" stroke-width="1.3"><rect x="1.5" y="3.5" width="13" height="9"/><path d="M1.5 3.5 8 9l6.5-5.5M1.5 12.5l5-4.5M14.5 12.5l-5-4.5"/></g></svg>lora@lorabetwick.co.nz</li>
    </ul>
  </div>
</section>

<section class="presentation presentation--painted">
  <div class="card card--front card--front-painted">
    <div class="front-painting" role="img" aria-label="Vintage watercolour painting of a wedding couple surrounded by pink and peach peonies"></div>
    <div class="logo-vertical logo-vertical--dark">
      <span class="logo-first">Lora</span>
      <span class="logo-last">Betwick</span>
    </div>
  </div>
  <div class="card card--back">
    <div class="logo-line">Lora Betwick</div>
    <ul class="contact-list">
      <li><svg viewBox="0 0 16 16" aria-hidden="true"><path d="M4 1.5c.7 0 1.4 2.6 1 3.2L3.8 5.8c.8 2 2.3 3.6 4.3 4.5l1.1-1.2c.6-.5 3.3.3 3.3 1v1.7c0 .8-.8 1.5-1.7 1.4C5.8 12.6 2.2 9 1.6 4.1 1.5 3.2 2.2 2.4 3 2.4z" fill="#1c1c1c"/></svg>+64 9 555 0147</li>
      <li><svg viewBox="0 0 16 16" aria-hidden="true"><g fill="none" stroke="#1c1c1c" stroke-width="1.3"><circle cx="8" cy="8" r="6.5"/><ellipse cx="8" cy="8" rx="3" ry="6.5"/><path d="M1.5 8h13M2.5 4.5h11M2.5 11.5h11"/></g></svg>lorabetwick.co.nz</li>
      <li><svg viewBox="0 0 16 16" aria-hidden="true"><g fill="none" stroke="#1c1c1c" stroke-width="1.3"><rect x="1.5" y="3.5" width="13" height="9"/><path d="M1.5 3.5 8 9l6.5-5.5M1.5 12.5l5-4.5M14.5 12.5l-5-4.5"/></g></svg>lora@lorabetwick.co.nz</li>
    </ul>
  </div>
</section>

</body>
</html>
```